Modern Stationary for Architecs
Orbit Architecs
Simple
Arch. Fahad Nabil Alqurashi
CEO
KSA
Riyadh
Alwurud -Prince Faisal Road
eng.qurashi@postvela.net
We are looking for a professional and attractive for our Stationary .
so we expect to see :
Letterhead
envelop
CD label & Jacket
Folder
Just logo
logo
Please us this file for all stationary
Please use this file in Letterhead ONLY

```html
<!DOCTYPE html>
<html lang="en">
<head>
<meta charset="utf-8">
<title>Orbit Architecs – Business Card</title>
<link href="https://fonts.googleapis.com/css2?family=Raleway:wght@500;600&family=Open+Sans:wght@400;600&display=swap" rel="stylesheet">
<style>
  :root{
    --page:#e6e7e9;
    --card-light:#fbfbfb;
    --card-shade:#dcdddf;
    --brand-red:#a3161c;
    --brand-red-dark:#7c0d12;
    --stripe-grey:#8e9094;
    --ink:#3b3d40;
    --ink-soft:#6a6c70;
    --white:#ffffff;
  }
  *{margin:0;padding:0;box-sizing:border-box}
  html,body{width:1200px;height:901px;overflow:hidden}
  body{background:var(--page);font-family:"Open Sans",Arial,sans-serif;color:var(--ink);position:relative}

  .card{position:absolute;left:250px;width:700px;height:400px;border-radius:24px;overflow:hidden;
        background:linear-gradient(135deg,var(--card-light) 0%,#f1f1f2 55%,var(--card-shade) 100%);
        box-shadow:0 12px 30px rgba(0,0,0,.18)}
  .card--back{top:30px}
  .card--front{top:466px}
  .card svg.card__shapes{position:absolute;inset:0}

  .brand{position:absolute;display:flex;align-items:center;gap:14px;white-space:nowrap}
  .brand__dot{width:22px;height:22px;border-radius:50%;background:var(--brand-red);flex:none}
  .brand__name{font-family:"Raleway",Arial,sans-serif;font-weight:600;color:var(--ink-soft);letter-spacing:.5px}
  .card--back .brand{left:50%;top:50%;transform:translate(-50%,-50%)}
  .card--back .brand__name{font-size:44px}
  .card--front .brand{left:58px;top:160px}
  .card--front .brand__name{font-size:34px}
  .card--front .brand__dot{width:18px;height:18px}

  .holder{position:absolute;right:40px;top:92px;text-align:right;color:var(--white);white-space:nowrap}
  .holder__name{font-size:16px;font-weight:600}
  .holder__role{font-size:12px;margin-top:2px}

  .address{position:absolute;left:58px;top:290px;font-size:14px;line-height:21px;color:var(--ink);font-style:normal}

  .contacts{position:absolute;left:440px;top:292px;list-style:none;font-size:14px;line-height:20px;color:var(--ink)}
  .contacts li{display:flex;align-items:center;gap:9px}
  .contacts svg{width:13px;height:13px;flex:none}
</style>
</head>
<body>

<section class="card card--back">
  <div class="brand"><span class="brand__dot"></span><span class="brand__name">Orbit Architecs</span></div>
</section>

<section class="card card--front">
  <svg class="card__shapes" viewBox="0 0 700 400" preserveAspectRatio="none" aria-hidden="true">
    <defs>
      <linearGradient id="redBand" x1="0" y1="0" x2="1" y2="1">
        <stop offset="0" stop-color="#b81e24"/>
        <stop offset="1" stop-color="#7c0d12"/>
      </linearGradient>
    </defs>
    <path d="M0,58 C200,74 420,150 560,184 C640,204 684,250 700,326" fill="none" stroke="#8e9094" stroke-width="9"/>
    <path d="M0,0 L700,0 L700,300 C680,230 640,190 560,170 C420,135 200,60 0,40 Z" fill="url(#redBand)"/>
  </svg>

  <div class="brand"><span class="brand__dot"></span><span class="brand__name">Orbit Architecs</span></div>

  <div class="holder">
    <p class="holder__name">Arch. Fahad Nabil Alqurashi</p>
    <p class="holder__role">CEO</p>
  </div>

  <address class="address">
    KSA<br>Riyadh<br>Alwurud -Prince Faisal Road
  </address>

  <ul class="contacts">
    <li><svg viewBox="0 0 16 16"><path fill="#a3161c" d="M3 1h3l1.5 4-2 1.2a9 9 0 0 0 4.3 4.3l1.2-2 4 1.5v3a2 2 0 0 1-2 2A13 13 0 0 1 1 3a2 2 0 0 1 2-2z"/></svg>00966110427 35</li>
    <li><svg viewBox="0 0 16 16"><rect x="4" y="1" width="8" height="14" rx="1.5" fill="#a3161c"/><rect x="5.5" y="3" width="5" height="8" fill="#fff"/></svg>966500731284</li>
    <li><svg viewBox="0 0 16 16"><rect x="1" y="6" width="14" height="8" rx="1" fill="#a3161c"/><rect x="4" y="1" width="8" height="6" fill="#a3161c"/><rect x="5" y="2" width="6" height="4" fill="#fff"/></svg>00966110427 35</li>
    <li><svg viewBox="0 0 16 16"><rect x="1" y="3" width="14" height="10" rx="1" fill="#a3161c"/><path d="M1.5 4l6.5 5 6.5-5" fill="none" stroke="#fff" stroke-width="1.3"/></svg>eng.qurashi@postvela.net</li>
  </ul>
</section>

</body>
</html>
```